Design Android App for Creating Estimates and Invoices

This project is to create a graphic design for an Android mobile app called Velmira Builder App which is an app that will help contractors to quickly create professional estimates and invoices, accept payments, manage clients and projects and run their business smoothly.

Link to some designs I created myself, hoping to get even better design from you
https://snapvault.example/album/qTrWpe

This project is similar to
https://appmarket.example/store/apps/details?id=com.brevlo.android.brevlo
https://appmarket.example/store/apps/details?id=com.tuvrq.quikbill

Check this Google Doc for more information. http://shrtn.example/8KmPqX4

Target Market(s)

Contractors, Home Improvement Professionals, Home Builders,

Industry/Entity Type

Residential Construction

Requirements
Must have
• Non-cluttered screen for Estimates, Enough white space between fields.
Nice to have
• Be different from the two example designs shown

```html
<!DOCTYPE html>
<html lang="en">
<head>
<meta charset="utf-8">
<title>Velmira Builder App – New Estimates</title>
<link rel="stylesheet" href="https://fonts.googleapis.com/css2?family=Roboto:wght@400;500&display=swap">
<style>
  :root {
    --page-bg: #dfe5f7;
    --status-blue: #2f5299;
    --bar-blue: #34589f;
    --heading-blue: #3f63b5;
    --surface: #f3f3f7;
    --card: #ffffff;
    --text: #222222;
    --muted: #555a63;
    --nav-grey: #8a90a0;
    --orange: #ff7a0d;
    --orange-dot: #ff6b00;
    --orange-halo: #ffe1cc;
    --green: #7ac81e;
    --green-knob: #7ed321;
    --green-track: #c8ea9e;
    --green-soft: #c5e39a;
    --grey-dot: #d3d3d8;
    --grey-line: #d8d8dc;
  }
  * { box-sizing: border-box; margin: 0; padding: 0; }
  html, body { width: 1200px; height: 1200px; overflow: hidden; }
  body { background: var(--page-bg); font-family: "Roboto", sans-serif; position: relative; }

  .app-screen {
    position: absolute; left: 269px; top: 10px;
    width: 576px; height: 1027px;
    transform: scale(1.15); transform-origin: top left;
    background: var(--surface); overflow: hidden;
    box-shadow: 0 10px 40px rgba(40,60,120,.18);
  }
  .status-bar {
    position: absolute; left: 0; top: 0; width: 100%; height: 38px;
    background: var(--status-blue); color: #fff;
    display: flex; align-items: center; justify-content: flex-end; gap: 8px; padding-right: 12px;
    font-size: 20px;
  }
  .app-bar {
    position: absolute; left: 0; top: 38px; width: 100%; height: 124px;
    background: var(--bar-blue); color: #fff;
  }
  .app-bar .back-icon { position: absolute; left: 22px; top: 48px; }
  .app-bar .title { position: absolute; left: 80px; top: 44px; font-size: 27px; font-weight: 500; }
  .app-bar .preview { position: absolute; left: 424px; top: 51px; font-size: 17px; letter-spacing: .5px; }
  .app-bar .search-icon { position: absolute; left: 525px; top: 44px; }

  .stepper { position: absolute; left: 0; top: 189px; }

  .payment-card {
    position: absolute; left: 22px; top: 266px; width: 531px; height: 393px;
    background: var(--card); box-shadow: 0 1px 4px rgba(0,0,0,.08); border-radius: 2px;
  }
  .payment-card h2 {
    position: absolute; left: 17px; top: 24px;
    font-size: 20px; font-weight: 400; color: var(--heading-blue);
  }
  .payment-card .divider { position: absolute; left: 17px; right: 17px; top: 68px; height: 1px; background: #ececef; }
  .option-row {
    position: absolute; left: 18px; right: 14px; height: 40px;
    display: flex; align-items: center; font-size: 20px; color: var(--text);
  }
  .option-row .help {
    display: inline-block; width: 20px; height: 20px; border-radius: 50%;
    background: #d5d5d9; color: #fff; font-size: 14px; text-align: center; line-height: 20px; margin-left: 14px;
  }
  .option-row .action { margin-left: auto; display: flex; align-items: center; gap: 22px; color: var(--green); }
  .toggle { margin-left: auto; position: relative; width: 40px; height: 24px; }
  .toggle .track { position: absolute; left: 0; top: 7px; width: 38px; height: 11px; border-radius: 6px; background: var(--green-track); }
  .toggle .knob { position: absolute; top: 2px; left: 18px; width: 21px; height: 21px; border-radius: 50%; background: var(--green-knob); }
  .toggle.off .track { background: #ececef; }
  .toggle.off .knob { left: 0; background: #bdbdc2; }

  .step-nav {
    position: absolute; left: 22px; right: 24px; top: 698px;
    display: flex; justify-content: space-between; font-size: 18px; color: var(--muted);
  }
  .step-nav span { display: flex; align-items: center; gap: 10px; }

  .btn {
    position: absolute; top: 868px; width: 238px; height: 52px;
    display: flex; align-items: center; justify-content: center; gap: 14px;
    color: #fff; font-size: 16px; font-weight: 500; border-radius: 2px;
  }
  .btn-save { left: 39px; background: var(--green-soft); }
  .btn-add { left: 299px; background: var(--orange); box-shadow: 0 2px 4px rgba(0,0,0,.15); }

  .bottom-nav {
    position: absolute; left: 0; top: 945px; width: 100%; height: 82px;
    background: #fff; display: flex;
  }
  .nav-item {
    flex: 1; display: flex; flex-direction: column; align-items: center; padding-top: 12px;
    font-size: 13px; letter-spacing: .4px; color: var(--nav-grey); gap: 8px;
  }
  .nav-item.active { color: var(--orange); }
</style>
</head>
<body>
<main class="app-screen">
  <div class="status-bar">
    <svg width="62" height="22" viewBox="0 0 62 22"><path d="M2 3 L26 3 L14 20Z" fill="#fff"/><path d="M34 20 L52 2 L52 20Z" fill="#fff"/><rect x="54" y="1" width="8" height="20" rx="1" fill="#fff" transform="translate(2,0)"/></svg>
    <span>12:30</span>
  </div>

  <header class="app-bar">
    <svg class="back-icon" width="30" height="24" viewBox="0 0 30 24"><path d="M28 12H3M13 2 3 12l10 10" stroke="#fff" stroke-width="2.4" fill="none"/></svg>
    <h1 class="title">New Estimates</h1>
    <span class="preview">PREVIEW</span>
    <svg class="search-icon" width="28" height="28" viewBox="0 0 28 28"><circle cx="11" cy="11" r="9" stroke="#fff" stroke-width="2.4" fill="none"/><path d="M18 18l8 8" stroke="#fff" stroke-width="2.4"/></svg>
  </header>

  <svg class="stepper" width="576" height="40" viewBox="0 0 576 40">
    <line x1="55" y1="20" x2="210" y2="20" stroke="var(--orange-dot)" stroke-width="1.5"/>
    <line x1="210" y1="20" x2="520" y2="20" stroke="var(--grey-line)" stroke-width="1.5"/>
    <g fill="var(--orange-halo)"><circle cx="55" cy="20" r="15"/><circle cx="132" cy="20" r="15"/><circle cx="210" cy="20" r="15"/></g>
    <g fill="#ececef"><circle cx="287" cy="20" r="12"/><circle cx="364" cy="20" r="12"/><circle cx="442" cy="20" r="12"/><circle cx="520" cy="20" r="12"/></g>
    <g fill="var(--orange-dot)"><circle cx="55" cy="20" r="7.5"/><circle cx="132" cy="20" r="7.5"/><circle cx="210" cy="20" r="7.5"/></g>
    <g fill="var(--grey-dot)"><circle cx="287" cy="20" r="7"/><circle cx="364" cy="20" r="7"/><circle cx="442" cy="20" r="7"/><circle cx="520" cy="20" r="7"/></g>
  </svg>

  <section class="payment-card">
    <h2>PAYMENT OPTION</h2>
    <div class="divider"></div>
    <div class="option-row" style="top:77px">Request a Deposit
      <span class="action">Add <svg width="26" height="26" viewBox="0 0 26 26"><circle cx="13" cy="13" r="11" stroke="var(--green)" stroke-width="2" fill="none"/><path d="M13 8v10M8 13h10" stroke="var(--green)" stroke-width="2"/></svg></span>
    </div>
    <div class="option-row" style="top:142px">Payment Schedule <span class="help">?</span>
      <span class="action">Add <svg width="26" height="26" viewBox="0 0 26 26"><circle cx="13" cy="13" r="11" stroke="var(--green)" stroke-width="2" fill="none"/><path d="M13 8v10M8 13h10" stroke="var(--green)" stroke-width="2"/></svg></span>
    </div>
    <div class="option-row" style="top:206px">Accept Credit Cards <span class="help">?</span>
      <span class="toggle"><span class="track"></span><span class="knob"></span></span>
    </div>
    <div class="option-row" style="top:270px">Accept E-Check <span class="help">?</span>
      <span class="toggle off"><span class="track"></span><span class="knob"></span></span>
    </div>
    <div class="option-row" style="top:334px">Show Financing Option
      <span class="toggle"><span class="track"></span><span class="knob"></span></span>
    </div>
  </section>

  <nav class="step-nav">
    <span><svg width="10" height="16" viewBox="0 0 10 16"><path d="M8 2 2 8l6 6" stroke="var(--muted)" stroke-width="2" fill="none"/></svg>Back</span>
    <span>Next<svg width="10" height="16" viewBox="0 0 10 16"><path d="M2 2l6 6-6 6" stroke="var(--muted)" stroke-width="2" fill="none"/></svg></span>
  </nav>

  <div class="btn btn-save"><svg width="18" height="14" viewBox="0 0 18 14"><path d="M1 7l5 5L17 1" stroke="#fff" stroke-width="2" fill="none"/></svg>SAVE ESTIMATES</div>
  <div class="btn btn-add"><svg width="18" height="18" viewBox="0 0 18 18"><path d="M9 1v16M1 9h16" stroke="#fff" stroke-width="2"/></svg>ADD NEW ESTIMATES</div>

  <nav class="bottom-nav">
    <div class="nav-item active">
      <svg width="28" height="32" viewBox="0 0 28 32"><rect x="2" y="1" width="24" height="30" rx="2" stroke="var(--orange)" stroke-width="2.4" fill="none"/><rect x="6" y="5" width="16" height="5" fill="var(--orange)"/><g fill="var(--orange)"><rect x="6" y="13" width="4" height="4"/><rect x="12" y="13" width="4" height="4"/><rect x="18" y="13" width="4" height="4"/><rect x="6" y="19" width="4" height="4"/><rect x="12" y="19" width="4" height="4"/><rect x="18" y="19" width="4" height="4"/><rect x="6" y="25" width="4" height="3"/><rect x="12" y="25" width="4" height="3"/><rect x="18" y="25" width="4" height="3"/></g></svg>
      ESTIMATES</div>
    <div class="nav-item">
      <svg width="40" height="32" viewBox="0 0 40 32"><rect x="2" y="5" width="36" height="22" stroke="var(--nav-grey)" stroke-width="2" fill="none"/><text x="20" y="21" font-size="12" text-anchor="middle" fill="var(--nav-grey)" font-family="Roboto, sans-serif">00$</text></svg>
      INVOICES</div>
    <div class="nav-item">
      <svg width="28" height="32" viewBox="0 0 28 32"><circle cx="14" cy="9" r="7" stroke="var(--nav-grey)" stroke-width="2" fill="none"/><path d="M2 31c0-8 5-13 12-13s12 5 12 13" stroke="var(--nav-grey)" stroke-width="2" fill="none"/></svg>
      CLIENTS</div>
    <div class="nav-item">
      <svg width="32" height="32" viewBox="0 0 32 32"><g fill="var(--nav-grey)"><rect x="2" y="26" width="4" height="4"/><rect x="9" y="20" width="4" height="10"/><rect x="16" y="14" width="4" height="16"/><rect x="23" y="6" width="4" height="24"/></g><path d="M2 14 10 6M6 4h5v5" stroke="var(--nav-grey)" stroke-width="2" fill="none"/></svg>
      REPORTS</div>
    <div class="nav-item">
      <svg width="32" height="32" viewBox="0 0 32 32"><circle cx="16" cy="16" r="5" stroke="var(--nav-grey)" stroke-width="2" fill="none"/><path d="M16 2v5M16 25v5M2 16h5M25 16h5M6 6l3.5 3.5M22.5 22.5 26 26M6 26l3.5-3.5M22.5 9.5 26 6" stroke="var(--nav-grey)" stroke-width="3"/><circle cx="16" cy="16" r="10" stroke="var(--nav-grey)" stroke-width="2" fill="none"/></svg>
      SETTINGS</div>
  </nav>
</main>
</body>
</html>
```